Corporate Design für Hotel und Restaurant inkl. Tagung, Biergarten
Zielgruppe
Hotel und Restaurant inkl. Tagung, Biergarten...
Zielgruppe sind Geschäftsreisende, Firmen und Familienfeiern mit Übernachtung
Aufgabenstellung
Moderner Schriftzug mit altem Logo siehe http://www.hotel-falkenauer-gut.de
und einen modernen Zusatz... Aber nicht Tagungshotel, Stadthotel o.ä.

```html
<!DOCTYPE html>
<html lang="de">
<head>
<meta charset="utf-8">
<title>Hotel Falkenauer Gut – Geschäftsausstattung</title>
<link href="https://fonts.googleapis.com/css2?family=Asap+Condensed:wght@300;400;500&display=swap" rel="stylesheet">
<style>
:root{
  --gold:#c9ac73;
  --grey:#6e6e6e;
  --text:#555555;
  --stage:#ececec;
  --paper:#ffffff;
  --ink:#000000;
}
*{margin:0;padding:0;box-sizing:border-box}
html,body{width:1200px;height:849px;overflow:hidden}
body{background:var(--stage);font-family:"Asap Condensed",sans-serif;font-weight:300;color:var(--text);position:relative}
.abs{position:absolute}

/* Wordmark lockup */
.brand-name{color:var(--gold);font-weight:500;display:inline-block;text-align:left}
.brand-name .line{display:flex;align-items:center;gap:8px;white-space:nowrap}
.brand-name .line + .line{padding-left:12px}
.brand-mark{display:inline-block;border:1.5px solid currentColor}
.brand-tag{color:var(--grey);white-space:nowrap;font-weight:400}

/* Letterhead */
.letter{left:51px;top:48px;width:532px;height:753px;background:var(--paper);border:5px solid var(--gold)}
.letter p{position:absolute;left:46px;font-size:9.5px;line-height:11.8px;white-space:nowrap}
.letter .brand{position:absolute;left:0;right:0;top:22px;text-align:center}
.letter .brand-name{font-size:30px;line-height:28px}
.letter .brand-mark{width:15px;height:15px}
.letter .brand-tag{font-size:6.8px;margin-top:4px}
.letter .sender{top:120px;font-size:6px;color:var(--grey);font-weight:400}
.sender .accent{color:var(--gold)}
.letter .date{left:379px;top:202px}
.footer-bar{position:absolute;top:717px;height:13px;width:33px;background:var(--gold)}
.footer-bar.left{left:0}.footer-bar.right{right:0}
.footer{position:absolute;top:719px;left:46px;display:flex;gap:18px;font-size:5.8px;line-height:7.8px;color:var(--grey);font-weight:400}
.fold{position:absolute;left:0;width:8px;height:1px;background:#cfcfcf}

/* Business cards */
.card{background:var(--paper);border:4px solid var(--gold)}
.card-back{left:560px;top:110px;width:296px;height:192px;transform:rotate(2.2deg);transform-origin:center}
.card-front{left:554px;top:118px;width:297px;height:193px}
.card .brand{position:absolute;left:0;right:0;top:16px;text-align:center}
.card .brand-name{font-size:27px;line-height:25px}
.card .brand-mark{width:13px;height:13px}
.card .brand-tag{font-size:7.2px;margin-top:4px}
.card-tab{left:-8px;top:126px;width:14px;height:20px;background:var(--gold)}
.person{left:19px;top:127px;line-height:11px}
.person .name{color:var(--gold);font-size:11px;font-weight:400}
.person .role{font-size:9px}
.contact{left:120px;top:105px;font-size:9.6px;line-height:14.3px;list-style:none}
.contact li{display:flex;align-items:flex-start;gap:6px;white-space:nowrap}
.contact svg{width:8px;height:8px;margin-top:3px;flex:none;fill:var(--gold)}
.contact .indent{padding-left:14px}

/* Logo variants */
.variant{left:907px;width:241px;height:89px}
.variant .brand{position:absolute;left:17px;top:10px}
.variant .brand-name{font-size:27px;line-height:25px}
.variant .brand-mark{width:13px;height:13px}
.variant .brand-tag{font-size:7.4px;margin-top:5px}
.v-white{top:290px;background:var(--paper)}
.v-grey{top:396px;background:var(--grey)}
.v-grey .brand-name,.v-grey .brand-tag{color:var(--gold)}
.v-gold{top:501px;background:var(--gold)}
.v-gold .brand-name,.v-gold .brand-tag{color:var(--grey)}
.v-mono{top:607px;background:var(--paper)}
.v-mono .brand-name,.v-mono .brand-tag{color:var(--ink)}
.v-black{top:712px;background:var(--ink)}
.v-black .brand-name,.v-black .brand-tag{color:var(--paper)}
</style>
</head>
<body>

<section class="abs letter" aria-label="Briefbogen">
  <div class="brand">
    <div class="brand-name"><span class="line">Hotel <span class="brand-mark"></span></span><span class="line">Falkenauer Gut</span></div>
    <div class="brand-tag">Ankommen · Tagen · Feiern | Ihr Haus im Grünen.</div>
  </div>
  <p class="sender"><span class="accent">Hotel Falkenauer Gut |</span> Lindenweg 9, 07743 Talheim</p>
  <p style="top:135px">Herrn<br>Max Mustermann<br>Musterallee 47<br>12345 Musterstadt</p>
  <p class="date">Talheim, den 17. Herbst 2017</p>
  <p style="top:210px">Buchungsbestätigung</p>
  <p style="top:245px">Sehr geehrter Herr Mustermann,</p>
  <p style="top:269px">schön, dass Sie sich für unser Haus entschieden haben.</p>
  <p style="top:293px">Wir freuen uns, Ihnen folgende Reservierung bestätigen zu können:</p>
  <p style="top:316px">Zeitraum: 28. - 30.09.2017<br>Gäste: 2<br>Anzahl der Zimmer: 1<br>Zimmerkategorie: Doppelzimmer, Standard<br>Preis: 199,00 Euro</p>
  <p style="top:387px">Frühstücksbuffet: inklusive<br>Zubuchbar: Halbpension 19,-€ pro Person</p>
  <p style="top:422px">Zahlungsmodalitäten:<br>Bar per EC- oder Kreditkarte</p>
  <p style="top:469px">Der Preis versteht sich pro Zimmer inkl. der gesetzlich gültigen Mehrwertsteuer und dem Bedienungsgeld.<br>Gern können Sie zum Preis von 2,00 Euro pro Fahrzeug &amp; Nacht unseren Parkplatz nutzen. Bitte beachten Sie das eine<br>Reservierung dazu nicht möglich ist.</p>
  <p style="top:517px">Das Zimmer steht Ihnen am Anreisetag ab 15:00 Uhr zur Verfügung. Unsere Rezeption ist bis 23:00 Uhr besetzt.<br>Sollte eine spätere Anreise nach 22:00 Uhr erfolgen, so bitten wir Sie uns telefonisch darüber zu informieren.</p>
  <p style="top:552px">Wir halten Ihre Zimmerreservierung auf garantierter Basis, eine kostenfreie Stornierung ist noch bis 24 Stunden vor<br>Anreise möglich. Bei späterer Stornierung oder Nichtanreise behält sich das Hotel das Recht vor, 90% der ersten Nacht in<br>Rechnung zu stellen.</p>
  <p style="top:599px">Wir freuen uns sehr, Sie bald in unserem Haus begrüßen zu dürfen und wünschen schon jetzt eine angenehme Anreise.</p>
  <p style="top:623px">Mit freundlichen Grüßen</p>
  <p style="top:647px">Ihr Team vom<br>Hotel Falkenauer Gut</p>
  <span class="fold" style="top:260px"></span>
  <span class="fold" style="top:527px"></span>
  <span class="footer-bar left"></span>
  <span class="footer-bar right"></span>
  <div class="footer">
    <div>Lindenweg 9<br>07743 Talheim</div>
    <div>Telefon 03 41 77 5 62 14<br>Fax 03 41 77 5 83 90</div>
    <div>info@hotel-falkenauer-gut.de<br>www.hotel-falkenauer-gut.de</div>
    <div>Steuer-Nr. &nbsp;162/430/07219<br>USt-IdNr. &nbsp;DE 987654321</div>
    <div>Sparkasse Talheim<br>IBAN DE41 2003 4455 0617 3382 00</div>
  </div>
</section>

<div class="abs card card-back" aria-hidden="true"></div>

<section class="abs card card-front" aria-label="Visitenkarte">
  <div class="brand">
    <div class="brand-name"><span class="line">Hotel <span class="brand-mark"></span></span><span class="line">Falkenauer Gut</span></div>
    <div class="brand-tag">Ankommen · Tagen · Feiern | Ihr Haus im Grünen.</div>
  </div>
  <span class="abs card-tab"></span>
  <div class="abs person">
    <div class="name">Stefan Kolleritz</div>
    <div class="role">Geschäftsführer</div>
  </div>
  <ul class="abs contact">
    <li><svg viewBox="0 0 10 10"><path d="M5 0a3.5 3.5 0 0 0-3.5 3.5C1.5 6 5 10 5 10s3.5-4 3.5-6.5A3.5 3.5 0 0 0 5 0zm0 5a1.4 1.4 0 1 1 0-2.8A1.4 1.4 0 0 1 5 5z"/></svg>Lindenweg 9</li>
    <li class="indent">07743 Talheim</li>
    <li><svg viewBox="0 0 10 10"><path d="M2 0l2 2.5-1 1.3a6 6 0 0 0 3.2 3.2l1.3-1L10 8 8.5 10C4 10 0 6 0 1.5z"/></svg>03 41 77 5 62 14
      <svg viewBox="0 0 10 10"><path d="M2.5 0h5v3h-5zM0 3.5h10v4H8V10H2V7.5H0zm3 3V9h4V6.5z"/></svg>03 41 77 5 83 90</li>
    <li><svg viewBox="0 0 10 10"><path d="M0 2h10v.8L5 6 0 2.8zm0 1.8l5 3.2 5-3.2V8H0z"/></svg>info@hotel-falkenauer-gut.de</li>
    <li><svg viewBox="0 0 10 10"><circle cx="5" cy="5" r="5"/></svg>www.hotel-falkenauer-gut.de</li>
  </ul>
</section>

<section class="abs variant v-white" aria-label="Logo positiv">
  <div class="brand"><div class="brand-name"><span class="line">Hotel <span class="brand-mark"></span></span><span class="line">Falkenauer Gut</span></div>
  <div class="brand-tag">Ankommen · Tagen · Feiern | Ihr Haus im Grünen.</div></div>
</section>
<section class="abs variant v-grey" aria-label="Logo auf Grau">
  <div class="brand"><div class="brand-name"><span class="line">Hotel <span class="brand-mark"></span></span><span class="line">Falkenauer Gut</span></div>
  <div class="brand-tag">Ankommen · Tagen · Feiern | Ihr Haus im Grünen.</div></div>
</section>
<section class="abs variant v-gold" aria-label="Logo auf Gold">
  <div class="brand"><div class="brand-name"><span class="line">Hotel <span class="brand-mark"></span></span><span class="line">Falkenauer Gut</span></div>
  <div class="brand-tag">Ankommen · Tagen · Feiern | Ihr Haus im Grünen.</div></div>
</section>
<section class="abs variant v-mono" aria-label="Logo schwarz">
  <div class="brand"><div class="brand-name"><span class="line">Hotel <span class="brand-mark"></span></span><span class="line">Falkenauer Gut</span></div>
  <div class="brand-tag">Ankommen · Tagen · Feiern | Ihr Haus im Grünen.</div></div>
</section>
<section class="abs variant v-black" aria-label="Logo negativ">
  <div class="brand"><div class="brand-name"><span class="line">Hotel <span class="brand-mark"></span></span><span class="line">Falkenauer Gut</span></div>
  <div class="brand-tag">Ankommen · Tagen · Feiern | Ihr Haus im Grünen.</div></div>
</section>

</body>
</html>
```